Healthcare IT firm needs classy and unique business care design

We need a business card design that incorporates our new logo design (attached) Prefer a purple based designed. I would really love to see something utilizing the "3D" version of the logo (purple on the reflective wall). I want something a little more than my logo printed along with a person's detailed contact information.
Contact Information for Business Card
Want something polished, professional, and a little unique in the design.
Colors
6b449b
Requirements
Must have
- Please use similar font as the logo design
Nice to have
- Would like to see the 3d version of my logo incorporated into the design.

```html
<!DOCTYPE html>
<html lang="en">
<head>
<meta charset="utf-8">
<title>Kinwell Health Systems – Business Card</title>
<link rel="stylesheet" href="https://fonts.googleapis.com/css2?family=Lato:wght@400;700&display=swap">
<style>
  :root {
    --backdrop: #c6c6c6;
    --card-dark: #0c0b0d;
    --brand-purple: #6b449b;
    --accent-purple: #7a4fb3;
    --text-grey: #a9a7ad;
    --rule-dark: #3a383d;
    --rule-light: #8e6fb8;
    --white: #ffffff;
  }
  * { margin: 0; padding: 0; box-sizing: border-box; }
  html, body {
    width: 1200px; height: 900px; overflow: hidden;
    background: var(--backdrop);
    font-family: "Lato", Arial, sans-serif;
  }
  .stage { position: relative; width: 1200px; height: 900px; }

  .card {
    position: absolute;
    width: 478px; height: 295px;
    box-shadow: 2px 3px 5px rgba(0,0,0,0.35);
  }
  .card-front {
    left: 120px; top: 275px;
    background: var(--card-dark);
    border-radius: 0 46px 0 46px;
  }
  .card-back {
    left: 606px; top: 273px;
    background: var(--brand-purple);
    border-radius: 46px 0 46px 0;
  }

  .brand-name {
    position: absolute;
    font-weight: 700;
    line-height: 1;
    text-align: center;
  }
  .card-front .brand-name {
    left: 224px; top: 72px; width: 220px;
    color: var(--accent-purple);
  }
  .card-back .brand-name {
    left: 128px; top: 110px; width: 222px;
    color: var(--white);
  }
  .brand-name .word { display: block; font-size: 46px; letter-spacing: -1px; }
  .brand-name .sub { display: block; font-size: 13px; letter-spacing: 1px; margin-top: 6px; }

  .person-name {
    position: absolute; left: 31px; top: 160px;
    font-size: 17px; color: var(--accent-purple);
  }
  .person-title {
    position: absolute; left: 33px; top: 181px;
    font-size: 13px; color: var(--text-grey);
  }
  .title-rule {
    position: absolute; left: 148px; top: 189px;
    width: 296px; height: 1px; background: var(--rule-dark);
  }
  .address {
    position: absolute; left: 31px; top: 235px;
    font-size: 13px; line-height: 17.5px; color: var(--text-grey);
  }
  .contact-list {
    position: absolute; right: 33px; top: 200px;
    list-style: none; text-align: right;
    font-size: 13px; line-height: 17.5px; color: var(--text-grey);
  }
  .contact-list li { display: flex; justify-content: flex-end; align-items: center; gap: 2px; }
  .contact-list svg { width: 11px; height: 11px; fill: var(--accent-purple); }

  .back-rule {
    position: absolute; left: 104px; top: 227px;
    width: 268px; height: 1px; background: var(--rule-light);
  }
  .back-web {
    position: absolute; left: 0; top: 247px; width: 100%;
    text-align: center; font-size: 13px; color: var(--white);
  }
</style>
</head>
<body>
<main class="stage">
  <section class="card card-front">
    <div class="brand-name"><span class="word">Kinwell</span><span class="sub">HEALTH SYSTEMS</span></div>
    <p class="person-name">Daniel Hart</p>
    <p class="person-title">Managing Director</p>
    <div class="title-rule"></div>
    <p class="address">12345, Address Goes Here<br>Country Name, 123456</p>
    <ul class="contact-list">
      <li>044-555 010 222
        <svg viewBox="0 0 12 12" aria-hidden="true"><path d="M1 4c0-2 2-3 5-3s5 1 5 3l-2 1-1-2H4L3 5zM3 6h6l1 5H2z"/></svg></li>
      <li>044-555 010 222
        <svg viewBox="0 0 12 12" aria-hidden="true"><path d="M3 0h6v12H3zM4 1.5v8h4v-8z"/></svg></li>
      <li>hello@kinwellhealth.com
        <svg viewBox="0 0 12 12" aria-hidden="true"><path d="M0 2h12v8H0zM1 3l5 4 5-4z" fill-rule="evenodd"/></svg></li>
      <li>www.kinwellhealth.com
        <svg viewBox="0 0 12 12" aria-hidden="true"><circle cx="6" cy="6" r="5.5"/></svg></li>
    </ul>
  </section>

  <section class="card card-back">
    <div class="brand-name"><span class="word">Kinwell</span><span class="sub">HEALTH SYSTEMS</span></div>
    <div class="back-rule"></div>
    <p class="back-web">www.kinwellhealth.com</p>
  </section>
</main>
</body>
</html>
```